Flyer for annual KESTREL SUMMIT 2020

I would like a church event flyer designed. The event is called "KESTREL SUMMIT 2020". I am looking for a professional, yet catchy design that uses our brand colors and logo creatively while communicating key information of the event effectively.

1. The logo is attached in two color formats. The designer has the choice to use them as he/she want.

2. The location of the event is: Harlow Community Center, 239 Fennimore Street, Portland, ME 04117

3. Time and date of event. The designer can organize and format the date and time as he/she pleases.
Thursday December 31st @ 6:30PM
Friday January 1st @ 6:30PM
Saturday 2nd @ 6:30PM
Sunday 3rd @ 4:30PM

4. The topic of the event is "In Fire and On Fire". The designer is free to use this phrase as he/she pleases to create a good composition.

5. Speaker: Prophet Marcus Olunde (2 pictures of the speaker to choose from are attached)

6. Contact information: contact@brightmeadowfold.org - Telephone number: 207 583 2914

7. I would also like the following three words on the flyer. These words describe the focus of the event: FIRE, REVIVAL, PROPHETIC

Target Market(s)

Young adults

Font styles to use
Sans Serif

Requirements
Must have
• Logo, speaker's picture
Should not have
• cross image, church image

```html
<!DOCTYPE html>
<html lang="en">
<head>
<meta charset="utf-8">
<title>Kestrel Summit 2020 Flyer</title>
<link rel="stylesheet" href="https://fonts.googleapis.com/css2?family=Oswald:wght@300;500;600;700&family=Cinzel:wght@400;500&family=Open+Sans:wght@400&display=swap">
<style>
  :root {
    --navy: #143a63;
    --orange: #f2932a;
    --gold: #c9a46a;
    --beige: #efe6dc;
    --paper: #ffffff;
    --stage: #eeeeee;
    --ink: #1d2a3a;
  }
  * { margin: 0; padding: 0; box-sizing: border-box; }
  html, body { width: 1200px; height: 776px; overflow: hidden; }
  body { background: var(--stage); position: relative; font-family: "Open Sans", sans-serif; }
  .flyer {
    position: absolute; left: 335px; top: 15px; width: 530px; height: 746px;
    background: var(--paper); overflow: hidden;
    box-shadow: 0 4px 14px rgba(0,0,0,0.18);
  }
  .backdrop { position: absolute; left: 0; top: 0; }
  .brand {
    position: absolute; right: 74px; top: 36px;
    font-family: "Cinzel", serif; font-weight: 500; font-size: 34px;
    color: var(--navy); letter-spacing: 1px;
  }
  .title { position: absolute; left: 272px; top: 176px; width: 245px; color: var(--navy); font-family: "Oswald", sans-serif; white-space: nowrap; }
  .title .main { display: block; font-weight: 600; font-size: 66px; line-height: 1; letter-spacing: -1px; }
  .title .sub { display: block; font-weight: 300; font-size: 52px; line-height: 1; margin-top: 8px; }
  .title .year { display: block; font-weight: 600; font-size: 112px; line-height: 1; margin-top: 6px; letter-spacing: -2px; }
  .focus {
    position: absolute; left: 35px; top: 396px; width: 205px; height: 205px;
    border-radius: 50%; background: var(--paper); border: 7px solid var(--navy);
    display: flex; flex-direction: column; justify-content: center; align-items: center;
    font-family: "Oswald", sans-serif; font-weight: 600; font-size: 30px; line-height: 1.22;
    color: var(--navy); white-space: nowrap;
  }
  .focus .accent { color: var(--orange); }
  .speaker { position: absolute; left: 258px; top: 500px; font-family: "Oswald", sans-serif; white-space: nowrap; }
  .speaker .label { display: block; font-weight: 600; font-size: 38px; line-height: 1; color: var(--navy); }
  .speaker .name { display: block; font-weight: 500; font-size: 22px; line-height: 1; color: var(--orange); margin-top: 8px; }
  .schedule { position: absolute; left: 258px; top: 600px; width: 260px; display: grid; grid-template-columns: 141px 119px; row-gap: 16px; }
  .session { display: flex; align-items: center; gap: 17px; }
  .session .num {
    width: 37px; height: 37px; flex: none; border-radius: 50%;
    border: 1.5px solid var(--navy); color: var(--navy);
    font-family: "Cinzel", serif; font-size: 22px; line-height: 34px; text-align: center;
  }
  .session .when { font-size: 9.5px; line-height: 1.25; color: var(--ink); white-space: nowrap; }
  .contact { position: absolute; left: 25px; top: 646px; color: var(--ink); }
  .contact h2 { font-family: "Cinzel", serif; font-weight: 400; font-size: 15px; letter-spacing: 0.5px; margin-bottom: 5px; }
  .contact p { font-size: 12.5px; line-height: 1.5; }
  .venue {
    position: absolute; left: 0; bottom: 0; width: 100%; height: 29px;
    background: var(--navy); color: #fff; font-size: 12.5px;
    display: flex; align-items: center; justify-content: center;
  }
</style>
</head>
<body>
  <main class="flyer">
    <svg class="backdrop" width="530" height="746" viewBox="0 0 530 746">
      <defs>
        <linearGradient id="hall" x1="0" y1="0" x2="1" y2="1">
          <stop offset="0" stop-color="#f3ece4"/>
          <stop offset="1" stop-color="#e6d8ca"/>
        </linearGradient>
        <linearGradient id="portrait" x1="0" y1="0" x2="0" y2="1">
          <stop offset="0" stop-color="#4a3a33"/>
          <stop offset="0.3" stop-color="#e35a2a"/>
          <stop offset="1" stop-color="#c9461f"/>
        </linearGradient>
      </defs>
      <ellipse cx="265" cy="291" rx="430" ry="199" fill="url(#hall)" stroke="var(--gold)" stroke-width="4" role="img" aria-label="Faint interior photo of the event hall"/>
      <rect x="5" y="29" width="262" height="459" rx="60" ry="60" fill="url(#portrait)" role="img" aria-label="Photo of the speaker in an orange suit and glasses"/>
    </svg>

    <div class="brand">ORVEN</div>

    <h1 class="title">
      <span class="main">KESTREL</span>
      <span class="sub">SUMMIT</span>
      <span class="year">2020</span>
    </h1>

    <div class="focus">
      <span>FIRE</span>
      <span class="accent">REVIVAL</span>
      <span>PROPHETIC</span>
    </div>

    <div class="speaker">
      <span class="label">SPEAKER</span>
      <span class="name">PROPHET MARCUS OLUNDE</span>
    </div>

    <div class="schedule">
      <div class="session"><span class="num">1</span><span class="when">THURSDAY<br>December 31st<br>6:30PM</span></div>
      <div class="session"><span class="num">2</span><span class="when">FRIDAY<br>January 1st<br>6:30PM</span></div>
      <div class="session"><span class="num">3</span><span class="when">SATURDAY<br>January 2nd<br>6:30PM</span></div>
      <div class="session"><span class="num">4</span><span class="when">SUNDAY<br>January 3rd<br>4:30PM</span></div>
    </div>

    <div class="contact">
      <h2>CONTACT US</h2>
      <p>207 583 2914<br>contact@brightmeadowfold.org</p>
    </div>

    <footer class="venue">Harlow Community Center, 239 Fennimore Street, Portland, ME 04117</footer>
  </main>
</body>
</html>
```